Non-governmental organisation branding design

We are looking to get the branding for our new NGO:

Tavelin Bridgework Centre

Our tag-line is: Peace through dialogue

We are a peace brokering organisation that conducts research and offers peace brokering services relating to conflicts around the world.

The branding needs to be simple, to the point and serious.

Other comparable organisations are:

https://www.qorvanhub.example/

http://zrt.example/

https://www.outerlumen.example/

Any questions, please get in touch.

Tavelin Bridgework Centre

1 page

```html
<!DOCTYPE html>
<html lang="en">
<head>
<meta charset="utf-8">
<title>Tavelin Bridgework Centre — Peace Through Dialogue</title>
<link href="https://fonts.googleapis.com/css2?family=Poppins:ital,wght@0,400;0,500;0,600;0,700;1,400&family=Roboto+Condensed:wght@400;700&display=swap" rel="stylesheet">
<style>
:root{
  --red:#c8102e;
  --navy:#2b3990;
  --ink:#1d1d1d;
  --body:#555;
  --grey-bg:#f2f2f2;
  --footer-bg:#eeeeee;
  --white:#fff;
}
*{box-sizing:border-box;margin:0;padding:0}
html,body{width:1200px;height:3939px;overflow:hidden}
body{position:relative;background:var(--white);font-family:'Poppins',sans-serif;color:var(--ink)}
.abs{position:absolute}
.heading{font-family:'Roboto Condensed',sans-serif;font-weight:700}

/* header */
.site-header{position:absolute;left:0;top:0;width:1200px;height:112px;background:var(--white)}
.brand{position:absolute;left:133px;top:20px;display:flex;align-items:center;gap:12px}
.brand-dot{width:58px;height:58px;border-radius:50%;background:var(--red)}
.brand-name{font-family:'Roboto Condensed',sans-serif;font-weight:700;font-size:23px;line-height:25px;color:var(--ink);text-transform:uppercase}
.call{position:absolute;left:722px;top:24px;display:flex;align-items:center;gap:10px;font-size:17px;color:var(--ink)}
.quote-btn{position:absolute;left:935px;top:17px;width:132px;height:36px;border-radius:18px;background:var(--navy);color:#fff;font-size:14px;font-weight:600;display:flex;align-items:center;justify-content:center}
.main-nav{position:absolute;left:482px;top:72px;display:flex;gap:24px;font-size:14.5px;font-weight:500;color:var(--ink)}
.main-nav .active{color:var(--red)}

/* hero */
.hero{position:absolute;left:0;top:112px;width:1200px;height:581px;background:
  radial-gradient(ellipse 260px 300px at 360px 230px,#c99b83 0%,rgba(201,155,131,0) 70%),
  radial-gradient(ellipse 300px 260px at 1000px 140px,#b89a86 0%,rgba(184,154,134,0) 70%),
  radial-gradient(ellipse 420px 300px at 700px 470px,#2b2f3d 0%,rgba(43,47,61,0) 75%),
  linear-gradient(120deg,#3a2f2a 0%,#6b5a4e 35%,#8f7b6c 55%,#4b4440 80%,#2c2a2a 100%)}
.hero-shade{position:absolute;inset:0;background:rgba(0,0,0,.22)}
.hero-title{position:absolute;left:0;width:1200px;top:272px;text-align:center;color:#fff;font-size:48px;letter-spacing:.5px}
.hero-btn{position:absolute;left:516px;top:352px;width:168px;height:36px;border:2px solid #fff;border-radius:18px;color:#fff;font-size:14px;font-weight:600;display:flex;align-items:center;justify-content:center}
.hero-arrow{position:absolute;top:268px;width:30px;height:30px;border-radius:50%;background:rgba(0,0,0,.55);display:flex;align-items:center;justify-content:center}

/* welcome */
.video{position:absolute;left:133px;top:797px;width:427px;height:308px}
.video-inner{position:absolute;left:8px;top:8px;width:403px;height:285px;background:
  radial-gradient(ellipse 120px 90px at 240px 160px,#8c7a6c 0%,rgba(140,122,108,0) 75%),
  radial-gradient(ellipse 200px 80px at 200px 40px,#e6e6e6 0%,rgba(230,230,230,0) 80%),
  linear-gradient(160deg,#c9c9c9,#8f8f8f 50%,#4e4e4e)}
.welcome-title{position:absolute;left:608px;top:792px;font-size:30px;line-height:42px;color:var(--ink);text-transform:uppercase}
.welcome-text{position:absolute;left:608px;top:886px;width:470px;font-size:12px;line-height:26px;color:var(--body)}
.btn-navy{position:absolute;left:610px;top:1068px;width:110px;height:33px;background:var(--navy);color:#fff;font-size:13px;font-weight:600;display:flex;align-items:center;justify-content:center;text-transform:uppercase}

/* mission */
.mission{position:absolute;left:0;top:1220px;width:1200px;height:558px;background:var(--grey-bg)}
.mission-title{position:absolute;left:0;top:88px;width:1200px;text-align:center;font-size:26px;font-weight:700;line-height:36px}
.mission-title .hl{color:var(--red)}
.mission-sub{position:absolute;left:0;top:132px;width:1200px;text-align:center;font-size:23px;font-weight:400}
.card{position:absolute;top:209px;width:222px;height:246px;background:#fff;border:1px solid #ddd;box-shadow:0 2px 6px rgba(0,0,0,.12);text-align:center}
.card-icon{width:92px;height:92px;border-radius:50%;background:var(--red);margin:22px auto 0;display:flex;align-items:center;justify-content:center}
.card-title{margin-top:16px;font-size:14px;font-weight:600;text-transform:uppercase}
.card-text{margin:10px auto 0;width:198px;font-size:11px;line-height:20px;color:var(--body)}

/* testimonial */
.testimonial{position:absolute;left:0;top:1778px;width:1200px;height:405px;background:linear-gradient(90deg,#3f4ea3,#4957ad 50%,#3f4ea3)}
.quote-box{position:absolute;left:293px;top:85px;width:617px;height:170px;background:#fff;border-radius:10px}
.quote-text{position:absolute;left:52px;top:18px;width:540px;font-size:11.5px;line-height:24px;font-style:italic;color:#555}
.qmark{position:absolute;font-family:Georgia,serif;font-size:36px;font-weight:700;color:#222;line-height:1}
.avatar{position:absolute;left:552px;top:225px;width:96px;height:96px;border-radius:50%;background:#fff;display:flex;align-items:center;justify-content:center}
.avatar-inner{width:78px;height:78px;border-radius:50%;background:var(--red)}
.t-name{position:absolute;top:282px;font-size:13px;color:#fff}

/* news */
.news-title{position:absolute;left:0;top:2266px;width:1200px;text-align:center;font-size:32px;font-weight:700;letter-spacing:.5px}
.news-card{position:absolute;width:447px;height:278px;overflow:hidden}
.news-photo{position:absolute;inset:0;background:
  radial-gradient(ellipse 90px 110px at 120px 110px,#c69477 0%,rgba(198,148,119,0) 75%),
  radial-gradient(ellipse 90px 110px at 330px 90px,#b88c70 0%,rgba(184,140,112,0) 75%),
  radial-gradient(ellipse 260px 80px at 220px 20px,#8a2f2a 0%,rgba(138,47,42,0) 80%),
  linear-gradient(150deg,#6d5a4d,#4a3f3a 50%,#262323)}
.news-photo.alt{background:
  radial-gradient(ellipse 80px 100px at 170px 100px,#b99580 0%,rgba(185,149,128,0) 75%),
  radial-gradient(ellipse 200px 90px at 300px 30px,#d6d6d6 0%,rgba(214,214,214,0) 80%),
  linear-gradient(150deg,#8f8f8f,#545454 50%,#252525)}
.news-shade{position:absolute;inset:0;background:linear-gradient(180deg,rgba(0,0,0,0) 40%,rgba(0,0,0,.7))}
.date{position:absolute;left:18px;top:170px;height:24px;padding:0 12px;background:var(--red);color:#fff;font-size:12px;display:flex;align-items:center;gap:6px}
.news-head{position:absolute;left:18px;top:206px;width:345px;font-size:14px;line-height:24px;font-weight:700;color:#fff;text-transform:uppercase}

/* subscribe */
.subscribe{position:absolute;left:0;top:3088px;width:1200px;height:407px;background:
  radial-gradient(ellipse 300px 160px at 250px 330px,#4a4440 0%,rgba(74,68,64,0) 80%),
  radial-gradient(ellipse 300px 160px at 950px 300px,#45403c 0%,rgba(69,64,60,0) 80%),
  linear-gradient(120deg,#2a2a2a,#3a3836 50%,#222)}
.sub-title{position:absolute;left:0;top:104px;width:1200px;text-align:center;color:#fff;font-size:35px;font-weight:700}
.sub-text{position:absolute;left:260px;top:162px;width:680px;text-align:center;color:#fff;font-size:15px;line-height:28px}
.sub-btn{position:absolute;left:510px;top:248px;width:180px;height:36px;border:2px solid #fff;border-radius:18px;color:#fff;font-size:15px;font-weight:600;display:flex;align-items:center;justify-content:center;text-transform:uppercase}

/* footer */
.site-footer{position:absolute;left:0;top:3495px;width:1200px;height:335px;background:var(--footer-bg)}
.f-brand{position:absolute;left:113px;top:62px;width:160px;text-align:center}
.f-brand .brand-dot{width:64px;height:64px;margin:0 auto 12px}
.f-brand .brand-name{font-size:19px;line-height:23px}
.socials{position:absolute;left:135px;top:222px;display:flex;gap:6px}
.socials span{width:24px;height:24px;border-radius:50%;border:1.5px solid #333}
.f-head{position:absolute;top:70px;font-size:17px;font-weight:700;text-transform:uppercase}
.f-head .hl{color:var(--red)}
.f-line{position:absolute;display:flex;gap:14px;font-size:13px;line-height:20px;color:#333}
.f-small{position:absolute;left:600px;top:115px;width:275px;font-size:10.5px;line-height:19px;color:#444}
.f-input{position:absolute;left:600px;top:166px;width:276px;height:36px;background:#fff;border:1px solid #ccc;border-radius:4px;font-size:11px;color:#888;padding-left:12px;display:flex;align-items:center}
.f-signup{position:absolute;left:600px;top:222px;width:116px;height:34px;background:var(--red);color:#fff;font-size:13px;font-weight:600;display:flex;align-items:center;justify-content:center;text-transform:uppercase}
.quick{position:absolute;left:947px;top:115px;list-style:none;font-size:12.5px;line-height:22.5px;color:#333}
.quick li::before{content:"";display:inline-block;border-left:5px solid #333;border-top:4px solid transparent;border-bottom:4px solid transparent;margin-right:10px}
.bottom-bar{position:absolute;left:0;top:3830px;width:1200px;height:109px;background:#fff;border-top:1px solid #ddd}
.copyright{position:absolute;left:0;top:44px;width:1200px;text-align:center;font-size:12.5px;color:#333}
</style>
</head>
<body>

<header class="site-header">
  <div class="brand"><span class="brand-dot"></span><span class="brand-name">Tavelin<br>Bridgework Centre</span></div>
  <div class="call">
    <svg width="18" height="18" viewBox="0 0 24 24"><path fill="#333" d="M6.6 10.8a15.1 15.1 0 006.6 6.6l2.2-2.2a1 1 0 011-.25 11.4 11.4 0 003.6.57 1 1 0 011 1V20a1 1 0 01-1 1A17 17 0 013 4a1 1 0 011-1h3.5a1 1 0 011 1c0 1.25.2 2.45.57 3.57a1 1 0 01-.25 1z"/></svg>
    <span>Call Us: 1300 555 014</span>
  </div>
  <div class="quote-btn">GET A QUOTE</div>
  <nav class="main-nav"><span class="active">HOME</span><span>SERVICES</span><span>RESOURCES</span><span>NEWS &amp; EVENTS</span><span>ABOUT US</span><span>CONTACT US</span></nav>
</header>

<section class="hero" role="img" aria-label="Photo of smiling delegates in conversation around a meeting table">
  <div class="hero-shade"></div>
  <div class="hero-arrow" style="left:100px"><svg width="12" height="12" viewBox="0 0 12 12"><path d="M8 2L4 6l4 4" stroke="#fff" stroke-width="2" fill="none"/></svg></div>
  <div class="hero-arrow" style="left:1068px"><svg width="12" height="12" viewBox="0 0 12 12"><path d="M4 2l4 4-4 4" stroke="#fff" stroke-width="2" fill="none"/></svg></div>
  <h1 class="hero-title heading">PEACE THROUGH DIALOGUE</h1>
  <div class="hero-btn">GET MORE INFO</div>
</section>

<section>
  <div class="video">
    <svg class="abs" style="left:0;top:0" width="427" height="308" viewBox="0 0 427 308" fill="none" stroke="#777" stroke-width="2">
      <path d="M1 40V1h50M376 1h50v40M426 268v39h-50M51 307H1v-39"/>
    </svg>
    <div class="video-inner" role="img" aria-label="Video still of a workshop group seated in an office">
      <svg class="abs" style="left:166px;top:107px" width="70" height="70" viewBox="0 0 70 70"><circle cx="35" cy="35" r="33" fill="#fff"/><circle cx="35" cy="35" r="27" fill="#222"/><path d="M29 23l17 12-17 12z" fill="#fff"/></svg>
    </div>
  </div>
  <h2 class="welcome-title heading">Welcome to<br>Tavelin Bridgework Centre</h2>
  <p class="welcome-text">Sed ut perspiciatis unde omnis iste natus error sit voluptatem accusantium doloremque laudantium, totam rem aperiam, eaque ipsa quae ab illo inore veritatis et quasi architecto beatae vitae dicta sunt explicabo. Nemo enim ipsam voluptatem quia voluptas sit aspernatur aut odit aut fugit, sed quia ntur magni dolores eos qui ratione voluptatem sequi nesciunt. Neque porro Sed ut perspiciatis unde omnis iste natus</p>
  <div class="btn-navy">Read More</div>
</section>

<section class="mission">
  <h2 class="mission-title"><span class="hl">THE TAVELIN BRIDGEWORK CENTRE</span> MISSION IS TO PREVENT, MITIGATE</h2>
  <p class="mission-sub">AND RESOLVE ARMED CONFLICTS, THROUGH DIALOGUE AND MEDIATION</p>
  <div class="card" style="left:133px"><div class="card-icon">
    <svg width="50" height="44" viewBox="0 0 50 44" fill="none" stroke="#fff" stroke-width="2.5" stroke-linejoin="round"><path d="M3 4h26v16H13l-6 6v-6H3z"/><path d="M33 14h14v16h-4v6l-6-6H21v-6"/></svg>
  </div><h3 class="card-title">Mediation and Dialogue</h3><p class="card-text">Sed ut perspiciatis unde omnis iste natus error sit voluptatem santium doloremque laudantium</p></div>
  <div class="card" style="left:370px"><div class="card-icon">
    <svg width="48" height="48" viewBox="0 0 48 48" fill="none" stroke="#fff" stroke-width="2.5"><circle cx="24" cy="24" r="20"/><ellipse cx="24" cy="24" rx="9" ry="20"/><path d="M4 24h40M8 13h32M8 35h32"/></svg>
  </div><h3 class="card-title">Mediation Expertise</h3><p class="card-text">Sed ut perspiciatis unde omnis iste natus error sit voluptatem santium doloremque laudantium</p></div>
  <div class="card" style="left:607px"><div class="card-icon">
    <svg width="40" height="50" viewBox="0 0 40 50" fill="none" stroke="#fff" stroke-width="2.5" stroke-linejoin="round"><rect x="3" y="6" width="34" height="41" rx="2"/><rect x="13" y="2" width="14" height="8" rx="1" fill="#c8102e"/><path d="M10 20l3 3 5-5M22 21h9M10 32l3 3 5-5M22 33h9"/></svg>
  </div><h3 class="card-title">Conflicts</h3><p class="card-text">Sed ut perspiciatis unde omnis iste natus error sit voluptatem santium doloremque laudantium</p></div>
  <div class="card" style="left:844px"><div class="card-icon">
    <svg width="48" height="44" viewBox="0 0 48 44" fill="none" stroke="#fff" stroke-width="2.5" stroke-linejoin="round"><path d="M24 40S4 28 4 15a9 9 0 0120-4 9 9 0 0120 4c0 13-20 25-20 25z"/><path d="M24 17v12M18 23h12"/></svg>
  </div><h3 class="card-title">Humanitarian Mediation</h3><p class="card-text">Sed ut perspiciatis unde omnis iste natus error sit voluptatem santium doloremque laudantium</p></div>
</section>

<section class="testimonial">
  <svg class="abs" style="left:152px;top:140px" width="22" height="44" viewBox="0 0 22 44"><path d="M20 2L3 22l17 20" stroke="#c9cdea" stroke-width="2" fill="none"/></svg>
  <svg class="abs" style="left:1026px;top:140px" width="22" height="44" viewBox="0 0 22 44"><path d="M2 2l17 20L2 42" stroke="#c9cdea" stroke-width="2" fill="none"/></svg>
  <div class="quote-box">
    <span class="qmark" style="left:22px;top:16px">&ldquo;</span>
    <p class="quote-text">Nemo enim ipsam voluptatem quia voluptas sit aspernatur aut odit aut fugit, sed quia conseq magni dolores eos qui ratione voluptatem sequi nesciunt. Neque porro quisquam est, qui do- lorem ipsum quia dolor sit amet, consectetur, adipisci velit, sed quia non numquam eius modi tempora incidunt ut labore et dolore magnam aliquam</p>
    <span class="qmark" style="left:380px;top:112px">&rdquo;</span>
  </div>
  <div class="avatar" role="img" aria-label="Portrait of the quoted speaker"><div class="avatar-inner"></div></div>
  <span class="t-name" style="left:450px">Noor Halden</span>
  <span class="t-name" style="left:662px">Tavelin Bridgework Centre</span>
</section>

<section>
  <h2 class="news-title">NEWS &amp; PRESS</h2>
  <article class="news-card" style="left:133px;top:2370px"><div class="news-photo" role="img" aria-label="Photo of a smiling crowd at an event"></div><div class="news-shade"></div><div class="date">&#9635; October 17, 2018</div><h3 class="news-head">Sed ut perspiciatis unde omnis iste natus error sit voluptatem accusantium</h3></article>
  <article class="news-card" style="left:620px;top:2370px"><div class="news-photo alt" role="img" aria-label="Photo of attendees talking at a reception"></div><div class="news-shade"></div><div class="date">&#9635; October 17, 2018</div><h3 class="news-head">Sed ut perspiciatis unde omnis iste natus error sit voluptatem accusantium</h3></article>
  <article class="news-card" style="left:133px;top:2682px"><div class="news-photo" role="img" aria-label="Photo of people applauding at a gathering"></div><div class="news-shade"></div><div class="date">&#9635; October 17, 2018</div><h3 class="news-head">Sed ut perspiciatis unde omnis iste natus error sit voluptatem accusantium</h3></article>
  <article class="news-card" style="left:620px;top:2682px"><div class="news-photo alt" role="img" aria-label="Photo of a seated working group in a meeting room"></div><div class="news-shade"></div><div class="date">&#9635; October 17, 2018</div><h3 class="news-head">Sed ut perspiciatis unde omnis iste natus error sit voluptatem accusantium</h3></article>
</section>

<section class="subscribe" role="img" aria-label="Dimmed photo of a conference audience behind the newsletter call">
  <h2 class="sub-title">SUBSCRIBE TO THE TBC NEWSLETTER</h2>
  <p class="sub-text">Sed ut perspiciatis unde omnis iste natus error sit voluptatem accusantium doloremque laudantium, totam rem aperiam, eaque ipsa quae ab illo inventore</p>
  <div class="sub-btn">Subscribe</div>
</section>

<footer class="site-footer">
  <div class="f-brand"><div class="brand-dot"></div><div class="brand-name">Tavelin<br>Bridgework Centre</div></div>
  <div class="socials"><span></span><span></span><span></span><span></span></div>

  <h4 class="f-head" style="left:320px">Contact <span class="hl">Us</span></h4>
  <div class="f-line" style="left:320px;top:118px"><svg width="12" height="16" viewBox="0 0 12 16"><path d="M6 0a6 6 0 00-6 6c0 4.5 6 10 6 10s6-5.5 6-10a6 6 0 00-6-6zm0 8.5A2.5 2.5 0 116 3.5a2.5 2.5 0 010 5z" fill="#c8102e"/></svg><span>Tavelin Bridgework Centre<br>Larkfield VIC 3990</span></div>
  <div class="f-line" style="left:320px;top:172px"><svg width="13" height="13" viewBox="0 0 24 24"><path fill="#c8102e" d="M6.6 10.8a15.1 15.1 0 006.6 6.6l2.2-2.2a1 1 0 011-.25 11.4 11.4 0 003.6.57 1 1 0 011 1V20a1 1 0 01-1 1A17 17 0 013 4a1 1 0 011-1h3.5a1 1 0 011 1c0 1.25.2 2.45.57 3.57a1 1 0 01-.25 1z"/></svg><span>Phone: 1300 555 014</span></div>
  <div class="f-line" style="left:320px;top:200px"><svg width="13" height="11" viewBox="0 0 13 11"><rect width="13" height="11" rx="1" fill="#c8102e"/><path d="M1 1l5.5 5L12 1" stroke="#fff" fill="none"/></svg><span>info@tavelinbridgework.example</span></div>

  <h4 class="f-head" style="left:600px">Sign up for <span class="hl">Newsletter</span></h4>
  <p class="f-small">Excepteur sint occaecat cupidatat non proident, sunt in culpa qui officia deserunt</p>
  <div class="f-input">Enter email</div>
  <div class="f-signup">Sign Up</div>

  <h4 class="f-head" style="left:943px">Quick <span class="hl">Links</span></h4>
  <ul class="quick"><li>Home</li><li>Services</li><li>Resources</li><li>News &amp; Events</li><li>About Us</li><li>Contact Us</li></ul>
</footer>

<div class="bottom-bar"><p class="copyright">Tavelin Bridgework Centre © 2018 All Rights Reserved | Privacy Policy | Terms and Conditions</p></div>

</body>
</html>
```